Brindle's Custom Signs and Woodworking Business Card

I run a small business that does custom woodworking and sign making. I have a logo already that I am very fond of, and would like to continue with the theme of the logo. I'd like a business card that adds onto that theme/design and stands out among typical business cards. As you'll be able to see from the logo, we're a patriotic brand and that is paramount to us.
Contact Information for Business Card
beneath the Brindle's logo, I'd like it to say
"Custom Signs & Woodworking"
Also, I'd like the following information template present on the card, preferably with the logos of instagram and facebook present besides the title.
(Name)                                 (Instragram)
(Email)                                  (Facebook)
(Phone)                                 (Website)
I would like for the name, email, and phone number to be editable so that I can have my employees utilize this card design as well. but for my card, my information is as follows
Dan "Brindle" Korvell, CEO                                           @BrindlesCustoms
Dan@BrindlesCustoms.example                                          Brindle's Customs
(555) 274-6103                                                         BrindlesCustoms.example
As for the back side, either a full american flag, or something that catches the eye, designer's preference I suppose.
Font styles to use
Other font styles liked:
- Funkydori, an adobe typekit font. it is the same as used for the logo. I'm not sure how the whole card will look with that, so if it doesn't look right please use something that complements the script style of the logo

```html
<!DOCTYPE html>
<html lang="en">
<head>
<meta charset="utf-8">
<title>Brindle's Custom Signs and Woodworking – Business Card</title>
<link rel="stylesheet" href="https://fonts.googleapis.com/css2?family=Ubuntu:wght@400;500;700&display=swap">
<style>
  :root {
    --backdrop: #2b2e32;
    --navy: #1f2d6e;
    --canton: #2c3557;
    --flag-red: #b8323a;
    --flag-tan: #cfae7e;
    --brand-red: #c51f33;
    --paper-white: #f1f1f1;
    --wood-grey-light: #e9e9e9;
    --wood-grey-mid: #cfcfcf;
    --ink: #3a3a3a;
    --ink-soft: #6a6a6a;
    --white: #ffffff;
  }
  * { box-sizing: border-box; margin: 0; padding: 0; }
  html, body {
    width: 1200px; height: 900px; overflow: hidden;
    background: var(--backdrop);
    font-family: "Ubuntu", sans-serif;
  }
  .canvas { position: relative; width: 1200px; height: 900px; }

  .card {
    position: absolute;
    width: 525px; height: 300px;
    overflow: hidden;
    box-shadow: 0 14px 30px rgba(0,0,0,.45);
  }

  /* Front */
  .card--front {
    left: 90px; top: 470px;
    background: linear-gradient(160deg, var(--wood-grey-light) 0%, var(--wood-grey-mid) 55%, #dcdcdc 100%);
  }
  .front__brand {
    position: absolute; left: 36px; top: 28px;
    font-weight: 700; font-size: 48px; line-height: 56px; color: var(--navy);
    letter-spacing: -0.5px;
  }
  .front__contact {
    position: absolute; left: 250px; top: 80px;
    color: var(--ink);
  }
  .contact__name {
    font-weight: 500; font-size: 18px; line-height: 22px; color: var(--brand-red);
  }
  .contact__title {
    font-size: 13px; line-height: 16px; color: var(--ink-soft); margin-bottom: 10px;
  }
  .contact__row {
    display: flex; align-items: center; gap: 8px;
    font-size: 16px; line-height: 24px;
  }
  .contact__icon { width: 14px; height: 14px; flex: none; }
  .front__band {
    position: absolute; left: 0; right: 0; bottom: 22px; height: 52px;
    background: var(--paper-white);
    display: flex; align-items: center; gap: 22px;
    padding-left: 38px;
  }
  .social {
    display: flex; align-items: center; gap: 7px;
    font-size: 13px; font-weight: 500; color: var(--brand-red);
  }
  .social__mark {
    width: 12px; height: 12px; background: var(--brand-red); border-radius: 3px;
  }
  .front__stripe {
    position: absolute; left: 0; right: 0; bottom: 0; height: 22px;
    background: var(--brand-red);
  }

  /* Back */
  .card--back { left: 590px; top: 130px; }
  .back__stripes {
    position: absolute; inset: 0;
    background: repeating-linear-gradient(180deg,
      var(--flag-red) 0 23.077px,
      var(--flag-tan) 23.077px 46.154px);
  }
  .back__canton {
    position: absolute; left: 0; top: 0;
    width: 210px; height: 161.5px;
    background: var(--canton);
  }
  .back__brand {
    position: absolute; left: 222px; top: 112px;
    font-weight: 700; font-size: 64px; line-height: 72px; color: var(--navy);
    letter-spacing: -1px;
  }
  .back__tagline {
    position: absolute; right: 28px; top: 231px;
    font-weight: 500; font-size: 16px; line-height: 22px; color: var(--white);
  }
</style>
</head>
<body>
<main class="canvas">

  <section class="card card--back" aria-label="Business card back">
    <div class="back__stripes"></div>
    <div class="back__canton" role="img" aria-label="Weathered star field of the American flag"></div>
    <div class="back__brand">Brindle's</div>
    <div class="back__tagline">Custom Signs &amp; Woodworking</div>
  </section>

  <section class="card card--front" aria-label="Business card front">
    <div class="front__brand">Brindle's</div>

    <div class="front__contact">
      <div class="contact__name">Dan "Brindle" Korvell</div>
      <div class="contact__title">CEO</div>
      <div class="contact__row">
        <svg class="contact__icon" viewBox="0 0 16 16" aria-hidden="true">
          <path fill="#c51f33" d="M3 1.5l2.5-.5 1.5 3.5-1.7 1.2a8 8 0 0 0 4.9 4.9l1.2-1.7 3.5 1.5-.5 2.5c-.2.8-1 1.3-1.8 1.1C6.8 13 3 9.2 1.9 3.3 1.7 2.5 2.2 1.7 3 1.5z"/>
        </svg>
        <span>(555) 274-6103</span>
      </div>
      <div class="contact__row">
        <svg class="contact__icon" viewBox="0 0 16 16" aria-hidden="true">
          <rect x="1" y="3" width="14" height="10" rx="1" fill="#c51f33"/>
          <path d="M1.5 3.8L8 9l6.5-5.2" fill="none" stroke="#f1f1f1" stroke-width="1.3"/>
        </svg>
        <span>Dan@BrindlesCustoms.example</span>
      </div>
      <div class="contact__row">
        <svg class="contact__icon" viewBox="0 0 16 16" aria-hidden="true">
          <circle cx="8" cy="8" r="6.5" fill="none" stroke="#c51f33" stroke-width="1.5"/>
          <ellipse cx="8" cy="8" rx="2.8" ry="6.5" fill="none" stroke="#c51f33" stroke-width="1.2"/>
          <path d="M1.5 8h13" stroke="#c51f33" stroke-width="1.2"/>
        </svg>
        <span>BrindlesCustoms.example</span>
      </div>
    </div>

    <div class="front__band">
      <div class="social"><span class="social__mark"></span>@BrindlesCustoms</div>
      <div class="social"><span class="social__mark"></span>Brindle's Customs</div>
    </div>
    <div class="front__stripe"></div>
  </section>

</main>
</body>
</html>
```